1. Need design for shock abosrber box.
2. attach is the old box model.

3. Brand: KORUVA
4. i want word: TOP DAMPERS (pls design unique font for this words)
to show strength and durability.

Box has 2 size:
1. 8cm x 8cm x 46cm
2. 22cm x 22cm x 46cm
(more or less)
Updates

Dear all,

1. TERAHOLT and attached file is old model box n design. We want new out of the box design.
2. KORUVA is the new brand. TOP DAMPERS is the slogan.
3. We attached some existing brands for your reference. Expecting a design that can top all those existing brand box design.

Dear All,

We would like to see something out of the box. You got to top the existing brands, which files i attached already.
Preference more to Kravholm style.

thanks,
Gordon.

Reason: 1. to give all designers enough time to submit quality design, i will extend the deadline 14 days.

Dear All,

In simple words, pls follow Kravholm concept for reference. I am ok with it.
I attached many pictures of Kravholm and you also can search easily in web.
I really expect something not too far from Kravholm concept.

Reason: Dear All, Please understand, i would like to give all designers enough time to submit their best design.

Font styles to use
Serif
Script

Colors
0491cc
34a7d8
86cae7
cee9f5
ecf7fb
ffffff

Requirements
Nice to have
• 1. area for car pictures (just like in old model box), that i can modify your file later on, with different car picture, depend on target car brand.

Wordings:
1. KORUVA TOP DAMPERS / KORUVA TOP DAMPER UNIT.
2. SUPER STRONG
3. MAXIMUM DURABILITY & PERFORMANCE.

can i have a japanese SUMO silhouette carrying a shock absorber. (if possible) at one side corner.

```html
<!DOCTYPE html>
<html lang="en">
<head>
<meta charset="utf-8">
<title>KORUVA Top Dampers – Box Artwork</title>
<link rel="stylesheet" href="https://fonts.googleapis.com/css2?family=Archivo+Black&family=Archivo:wght@400;600;700&display=swap">
<style>
  :root {
    --bg-light: #f4f4f4;
    --bg-mid: #d6d6d6;
    --metal-light: #6b6a66;
    --metal-mid: #55544f;
    --metal-dark: #3b3a37;
    --rule-gold: #a8916b;
    --rule-dark: #1f1f1d;
    --ink-white: #ffffff;
    --ink-soft: #e9e9e6;
    --ink-dark: #161615;
    --photo-light: #c9c9c7;
    --photo-dark: #7d7c78;
  }
  * { box-sizing: border-box; margin: 0; padding: 0; }
  html, body { width: 1200px; height: 1000px; overflow: hidden; }
  body {
    background: radial-gradient(ellipse at 55% 40%, var(--bg-light) 0%, var(--bg-mid) 100%);
    font-family: "Archivo", Arial, sans-serif;
    position: relative;
  }
  .panel {
    position: absolute;
    background:
      linear-gradient(160deg, rgba(255,255,255,0.08) 0%, rgba(0,0,0,0) 40%, rgba(255,255,255,0.06) 70%, rgba(0,0,0,0.12) 100%),
      linear-gradient(180deg, var(--metal-light) 0%, var(--metal-mid) 50%, var(--metal-dark) 100%);
    overflow: hidden;
    box-shadow: 0 0 0 1px rgba(0,0,0,0.35);
  }
  .rule {
    position: absolute; left: 0; right: 0; height: 4px;
    background: var(--rule-gold);
    border-top: 1px solid var(--rule-dark);
    border-bottom: 1px solid var(--rule-dark);
  }
  .heavy { font-family: "Archivo Black", Arial, sans-serif; color: var(--ink-white); line-height: 0.9; }
  .brand-name { font-family: "Archivo Black", Arial, sans-serif; color: var(--ink-white); letter-spacing: 1px; }
  .tagline { font-weight: 700; color: var(--ink-dark); }
  .web { font-size: 9px; color: var(--ink-soft); letter-spacing: 1px; }
  .product-photo {
    position: absolute;
    background: linear-gradient(160deg, var(--photo-light) 0%, var(--photo-dark) 100%);
  }
  .seal {
    position: absolute; border-radius: 50%;
    background: var(--ink-dark); border: 3px solid var(--rule-gold);
  }

  /* top face */
  .top-face { left: 250px; top: 260px; width: 900px; height: 220px; }
  .top-face .rule.upper { top: 44px; }
  .top-face .rule.lower { bottom: 44px; }
  .top-face .unit-label { position: absolute; left: 30px; top: 84px; font-size: 26px; transform: rotate(-4deg); }
  .top-face .brand-block { position: absolute; left: 330px; top: 62px; text-align: center; }
  .top-face .brand-block .brand-name { font-size: 64px; line-height: 1; }
  .top-face .brand-block .slogan { font-family: "Archivo Black", Arial, sans-serif; color: var(--ink-white); font-size: 13px; letter-spacing: 9px; }
  .top-face .brand-block .tagline { font-size: 12px; margin-top: 8px; color: var(--ink-white); }
  .top-face .web { position: absolute; right: 40px; top: 20px; }
  .top-face .seal { right: 40px; top: 74px; width: 72px; height: 72px; }

  /* side face */
  .side-face { left: 250px; top: 480px; width: 900px; height: 220px; }
  .side-face .rule.upper { top: 14px; }
  .side-face .rule.lower { bottom: 40px; }
  .side-face .title { position: absolute; left: 30px; top: 56px; display: flex; align-items: flex-end; gap: 14px; }
  .side-face .title .brand-name { font-size: 30px; margin-bottom: 36px; }
  .side-face .title .heavy { font-size: 52px; }
  .side-face .claim { position: absolute; left: 250px; top: 160px; font-size: 11px; color: var(--ink-white); font-style: italic; }
  .side-face .tagline { position: absolute; left: 30px; bottom: 12px; font-size: 18px; }
  .side-face .product-photo { left: 600px; top: 32px; width: 200px; height: 112px; }
  .side-face .seal { right: 24px; top: 40px; width: 58px; height: 58px; }
  .side-face .web { position: absolute; right: 40px; bottom: 56px; }

  /* end face */
  .end-face { left: 30px; top: 480px; width: 220px; height: 220px; }
  .end-face .rule.upper { top: 14px; }
  .end-face .rule.lower { bottom: 40px; }
  .end-face .brand-name { position: absolute; left: 14px; top: 30px; font-size: 17px; }
  .end-face .product-photo { left: 110px; top: 26px; width: 96px; height: 30px; }
  .end-face .heavy { position: absolute; left: 14px; top: 66px; font-size: 26px; }
  .end-face .details { position: absolute; right: 14px; top: 128px; text-align: right; font-size: 12px; color: var(--ink-white); font-weight: 700; line-height: 1.1; }
  .end-face .web { position: absolute; left: 0; right: 0; bottom: 16px; text-align: center; }
</style>
</head>
<body>

  <section class="panel top-face" aria-label="Top face">
    <div class="rule upper"></div>
    <div class="rule lower"></div>
    <div class="heavy unit-label">TOP DAMPER<br>UNIT</div>
    <div class="brand-block">
      <div class="brand-name">KORUVA</div>
      <div class="slogan">TOP DAMPERS</div>
      <div class="tagline">Super Strong ● Maximum durability &amp; performance.</div>
    </div>
    <div class="web">www.koruva.com</div>
    <div class="seal" role="img" aria-label="Quality seal"></div>
  </section>

  <section class="panel side-face" aria-label="Long side face">
    <div class="rule upper"></div>
    <div class="rule lower"></div>
    <div class="title">
      <span class="brand-name">KORUVA</span>
      <span class="heavy">TOP DAMPER<br>UNIT</span>
    </div>
    <div class="claim">Maximum durability &amp; performance.</div>
    <div class="tagline">Super Strong ● Maximum durability &amp; performance.</div>
    <div class="product-photo" role="img" aria-label="Product photo area: chrome shock absorber"></div>
    <div class="seal" role="img" aria-label="Quality seal"></div>
    <div class="web">www.koruva.com</div>
  </section>

  <section class="panel end-face" aria-label="End face">
    <div class="rule upper"></div>
    <div class="rule lower"></div>
    <div class="brand-name">KORUVA</div>
    <div class="product-photo" role="img" aria-label="Product photo area: chrome shock absorber"></div>
    <div class="heavy">TOP DAMPER<br>UNIT</div>
    <div class="details">Super Strong<br>Maximum durability<br>&amp; performance.</div>
    <div class="web">www.koruva.com</div>
  </section>

</body>
</html>
```